Harvest Gathering event flyer

I would like a church event flyer designed. The event is called "HARVEST GATHERING 2018". I am looking for a professional, yet catchy design that uses our brand colors and logo creatively while communicating key information of the event effectively.

1. The logo is attached in two color formats. The designer has the choice to use them as he/she want.

2. The location of the event is: Lindqvist Community Center, 482 Tamsworth Street, Portland, ME 04102
3. Time and date of event. The designer can organize and format the date and time as he/she pleases.
December 28th, 29th @ 7:00PM
December 30th @ 10:00AM
4. The topic of the event is "Tongues of fire". The designer is free to use this phrase as he/she pleases to create a good composition.
5. Speaker: Prophet Marcus Obuya
6. Contact information: contact@cedarbrookfellowship.org - Telephone number: 207 555 0148

7. I would also like the following three words on the flyer. These words describe the focus of the event: FIRE, REVIVAL, PROPHETIC

```html
<!DOCTYPE html>
<html lang="en">
<head>
<meta charset="utf-8">
<title>Harvest Gathering 2018 – Event Flyer</title>
<link href="https://fonts.googleapis.com/css2?family=Open+Sans:wght@400;600;700&family=Dancing+Script:wght@600&family=Cinzel:wght@500&display=swap" rel="stylesheet">
<style>
  :root{
    --navy:#0c3a62;
    --navy-deep:#0a3158;
    --orange:#f7931e;
    --gold-light:#fbf1c8;
    --gold:#e9b52a;
    --gold-deep:#b87a12;
    --white:#ffffff;
    --ink:#3b3b3b;
  }
  *{box-sizing:border-box;margin:0;padding:0}
  html,body{width:882px;height:1200px;overflow:hidden;background:#e9e9e9}
  .flyer{position:relative;width:882px;height:1200px;background:var(--white);font-family:"Open Sans",Arial,sans-serif;overflow:hidden}

  /* hero */
  .hero{position:absolute;left:0;top:0;width:882px;height:470px;
    background:linear-gradient(90deg,var(--gold-light) 0%,#f6dc86 30%,var(--gold) 58%,var(--gold-deep) 100%)}
  .hero-glow{position:absolute;inset:0;background:radial-gradient(circle at 30% 20%,rgba(255,255,255,.7),rgba(255,255,255,0) 55%)}
  .brand{position:absolute;left:30px;top:58px;display:flex;align-items:center;gap:10px}
  .brand-dot{width:22px;height:22px;border-radius:50%;background:var(--orange)}
  .brand-name{font-family:"Cinzel",Georgia,serif;font-weight:500;font-size:50px;color:var(--navy);letter-spacing:1px}
  .event-title{position:absolute;left:30px;top:180px;font-family:"Dancing Script",cursive;font-weight:600;color:var(--navy);font-size:64px;line-height:1.15}
  .event-title .year{display:block;padding-left:105px;font-size:78px}
  .speaker{position:absolute;left:0;top:400px;width:520px;height:44px;
    background:linear-gradient(90deg,rgba(255,240,200,.95),rgba(255,240,200,0));
    padding-left:18px;line-height:44px;font-weight:700;font-size:23px;color:var(--navy)}

  /* topic band */
  .topic{position:absolute;left:0;top:468px;width:882px;height:350px}
  .topic svg{position:absolute;inset:0}
  .ribbon{position:absolute;left:50%;transform:translateX(-50%);background:var(--orange);color:var(--navy);
    font-weight:700;text-align:center;clip-path:polygon(0 0,100% 0,96% 50%,100% 100%,0 100%,4% 50%)}
  .ribbon.topic-label{top:90px;width:290px;height:42px;line-height:42px;font-size:24px}
  .topic-title{position:absolute;top:140px;width:100%;text-align:center;color:var(--white);font-weight:600;font-size:70px;letter-spacing:12px}
  .focus{position:absolute;top:245px;width:100%;text-align:center;color:var(--white);font-size:23px;font-weight:600}
  .focus span::before{content:"";display:inline-block;width:10px;height:10px;border-radius:50%;background:var(--orange);margin:0 8px 3px 12px}

  /* calendar */
  .ribbon.calendar-label{top:862px;width:420px;height:42px;line-height:42px;font-size:25px}
  .dates{position:absolute;top:940px;left:37px;display:flex;gap:24px}
  .date-box{position:relative;width:254px;height:72px;border:3px solid var(--navy);text-align:center}
  .date-box .day{position:absolute;top:-20px;left:50%;transform:translateX(-50%);background:var(--white);padding:0 8px;
    color:var(--orange);font-weight:700;font-size:23px;white-space:nowrap}
  .date-box .time{margin-top:22px;font-size:22px;color:var(--navy)}

  /* contact */
  .venue{position:absolute;left:32px;top:1070px;display:flex;gap:12px;font-weight:700;font-size:21px;color:var(--ink);line-height:1.3}
  .venue address{font-style:normal;text-align:center}
  .contacts{position:absolute;left:478px;top:1068px;width:345px;font-weight:600;font-size:17px;color:var(--ink);line-height:1.7}
  .contacts li{list-style:none;display:flex;align-items:center;gap:8px;justify-content:center;white-space:nowrap}
  .social{position:absolute;left:838px;top:1056px;display:flex;flex-direction:column;gap:10px}
  .social span{width:28px;height:28px;border-radius:50%;background:var(--navy)}
  .footer-bar{position:absolute;left:0;bottom:0;width:882px;height:34px;display:flex}
  .footer-bar .navy{flex:0 0 440px;background:var(--navy)}
  .footer-bar .orange{flex:1;background:var(--orange)}
</style>
</head>
<body>
<main class="flyer">
  <section class="hero" role="img" aria-label="Photograph of a woman praying with clasped hands in warm golden sunlight beneath trees">
    <div class="hero-glow"></div>
  </section>
  <div class="brand"><span class="brand-dot"></span><span class="brand-name">KAVRO</span></div>
  <h1 class="event-title">Harvest Gathering<span class="year">2018</span></h1>
  <p class="speaker">SPEAKER : Prophet Marcus Obuya</p>

  <section class="topic">
    <svg width="882" height="350" viewBox="0 0 882 350" aria-hidden="true">
      <polygon points="0,0 882,0 882,12 0,22" fill="var(--orange)"/>
      <polygon points="0,22 882,12 882,338 0,338" fill="var(--navy-deep)"/>
      <line x1="0" y1="22" x2="882" y2="10" stroke="var(--white)" stroke-width="3"/>
      <polygon points="100,340 882,340 882,350 600,350" fill="var(--orange)"/>
    </svg>
    <div class="ribbon topic-label">EVENT TOPIC</div>
    <h2 class="topic-title">Tongues of fire</h2>
    <p class="focus"><span>FIRE</span><span>REVIVAL</span><span>PROPHETIC</span></p>
  </section>
  <svg style="position:absolute;left:0;top:808px" width="882" height="30" aria-hidden="true">
    <polygon points="90,8 882,8 882,30" fill="var(--orange)"/>
  </svg>

  <div class="ribbon calendar-label">CALENDER OF EVENTS</div>
  <div class="dates">
    <div class="date-box"><span class="day">December 28th</span><p class="time">7:00PM</p></div>
    <div class="date-box"><span class="day">December 29th</span><p class="time">7:00PM</p></div>
    <div class="date-box"><span class="day">December 30th</span><p class="time">10:00AM</p></div>
  </div>

  <div class="venue">
    <svg width="30" height="30" viewBox="0 0 30 30" aria-hidden="true"><circle cx="15" cy="15" r="13" fill="none" stroke="var(--orange)" stroke-width="2"/><path d="M15 23c-4-5-6-7.5-6-10a6 6 0 0 1 12 0c0 2.5-2 5-6 10z" fill="none" stroke="var(--orange)" stroke-width="2"/><circle cx="15" cy="13" r="2" fill="var(--orange)"/></svg>
    <address>Lindqvist Community Center, 482<br>Tamsworth Street, Portland<br>ME 04102</address>
  </div>
  <ul class="contacts">
    <li><svg width="16" height="16" viewBox="0 0 16 16" aria-hidden="true"><path d="M3 1l3 3-2 2c1 2 3 4 5 5l2-2 3 3-2 3C7 15 1 9 1 3z" fill="var(--orange)"/></svg>207 555 0148</li>
    <li><svg width="18" height="14" viewBox="0 0 18 14" aria-hidden="true"><rect width="18" height="14" rx="1" fill="var(--orange)"/><path d="M1 1l8 6 8-6" fill="none" stroke="#fff" stroke-width="1.5"/></svg>contact@cedarbrookfellowship.org</li>
    <li><svg width="16" height="16" viewBox="0 0 16 16" aria-hidden="true"><g fill="none" stroke="var(--orange)" stroke-width="1.5"><circle cx="8" cy="8" r="7"/><ellipse cx="8" cy="8" rx="3" ry="7"/><path d="M1 8h14"/></g></svg>www.kavro.org</li>
  </ul>
  <div class="social" aria-hidden="true"><span></span><span></span><span></span></div>

  <div class="footer-bar"><div class="navy"></div><div class="orange"></div></div>
</main>
</body>
</html>
```